Civic Counsel and Advocacy Network needs poster design for landlord/tenant cases

We're seeking a poster design (11x17) to spread awareness for services by "Civic Counsel and Advocacy Network". The services they're trying to communicate are regarding housing/landlord/tenant matters.

We'd like the poster to (1) reflect the color scheme and branding of their website www.ccanmorvale.org, (2) contain the following copy: "Everyone needs safe and suitable housing, whether they own a home or rent one. When homelessness threatens, we at CCN help clients free of charge through eviction diversion programs and mortgage/tax foreclosure prevention.", and (3) contain their contact information:

Civic Counsel and Advocacy Network, Inc.
"We are YOUR Law Firm for Housing matters"
Contact us at: (555) 314-2869
housing @ccanmorvale.org
www.ccanmorvale.org

Target Market(s)

People who may be facing eviction or homelessness

Industry/Entity Type

Legal

Colors
0054AA
0677BA
7BADD7
CADEEF
E8F1F8
FFC000
F8CF3A
FAE287
FDF2CF
FEFAEE
EB3D1F
EC4F4E
F09395
F8D3D4
FCEDEE

Requirements
Must have
• Must include colors from website: https://ccanmorvale.org/

```html
<!DOCTYPE html>
<html lang="en">
<head>
<meta charset="utf-8">
<title>Eviction Help Poster – Civic Counsel and Advocacy Network</title>
<link rel="stylesheet" href="https://fonts.googleapis.com/css2?family=Stardos+Stencil:wght@700&family=Arimo:wght@400;700&family=Libre+Baskerville&family=Roboto+Condensed&display=swap">
<style>
  :root {
    --canvas: #ffffff;
    --coral: #cd5f4c;
    --title-ink: #f4e8e2;
    --paper: #ededeb;
    --paper-shade: #dcdcda;
    --navy: #2f4487;
    --gold: #c9a24a;
    --white: #ffffff;
    --ink: #1b1b1b;
  }
  * { box-sizing: border-box; margin: 0; padding: 0; }
  html, body {
    width: 1200px; height: 1200px; overflow: hidden;
    background: var(--canvas);
  }
  .poster {
    position: absolute; left: 230px; top: 36px;
    width: 740px; height: 1128px;
    background: var(--navy);
    overflow: hidden;
  }
  .band-top {
    position: absolute; left: 0; top: 0; width: 740px; height: 340px;
    background: var(--coral);
  }
  .title-frame {
    position: absolute; left: 48px; top: 47px; width: 645px; height: 204px;
    border: 2px solid var(--title-ink);
    outline: 1px solid rgba(244,232,226,.5); outline-offset: -6px;
  }
  .title {
    position: absolute; left: 50%; top: 50%;
    font-family: "Stardos Stencil", "Times New Roman", serif;
    font-weight: 700; font-size: 220px; line-height: 1;
    white-space: nowrap; color: var(--title-ink);
    transform: translate(-50%, -50%) scale(0.62, 1);
  }
  .photo {
    position: absolute; left: 0; top: 300px; width: 740px; height: 420px;
    background: linear-gradient(90deg, #e2bd3a 0%, #e2bd3a 19%, #e6e8e6 21%, #d9dcd9 38%, #b99a6d 45%, #a88c68 60%, #c9a995 70%, #e0776a 85%, #8b8f96 100%);
  }
  .torn { position: absolute; left: 0; width: 740px; display: block; }
  .torn-coral { top: 290px; height: 70px; }
  .torn-paper { top: 680px; height: 60px; }
  .torn-navy { top: 860px; height: 60px; }
  .paper-strip {
    position: absolute; left: 0; top: 720px; width: 740px; height: 160px;
    background: var(--paper);
  }
  .quote {
    position: absolute; left: 40px; top: 733px; width: 660px;
    font-family: "Arimo", Arial, sans-serif; font-size: 15px; line-height: 23px;
    color: var(--ink); text-align: center;
  }
  .quote strong { font-weight: 700; }
  .quote .mark { font-weight: 700; font-size: 26px; line-height: 0; position: relative; }
  .quote .open { top: 2px; margin-right: 4px; }
  .quote .close { top: 12px; margin-left: 4px; }
  .brand {
    position: absolute; left: 48px; top: 896px;
    display: flex; align-items: center; gap: 16px;
  }
  .brand-dot {
    width: 82px; height: 82px; border-radius: 50%;
    border: 3px solid var(--white);
  }
  .brand-name {
    font-family: "Libre Baskerville", Georgia, serif; font-weight: 400;
    font-size: 16px; line-height: 21px; letter-spacing: 1px;
    color: var(--white); text-transform: uppercase;
  }
  .tagline {
    position: absolute; left: 543px; top: 886px; width: 152px; height: 116px;
    border-left: 1.5px solid var(--gold); border-bottom: 1.5px solid var(--gold);
    padding: 14px 0 0 12px;
    font-family: "Arimo", Arial, sans-serif; font-size: 16px; line-height: 22px;
    color: var(--gold);
  }
  .tagline::before {
    content: ""; position: absolute; left: 0; top: 0; width: 67px;
    border-top: 1.5px solid var(--gold);
  }
  .tagline strong { font-weight: 700; }
  .contact-line {
    position: absolute; left: 48px; top: 1033px; width: 390px; height: 45px;
    border-top: 1.5px solid var(--gold); border-bottom: 1.5px solid var(--gold);
    display: flex; align-items: center; gap: 6px;
    font-family: "Arimo", Arial, sans-serif; font-weight: 700; font-size: 22px;
    color: var(--gold); white-space: nowrap;
  }
  .contact-line svg { width: 22px; height: 22px; margin: 0 3px -3px 0; }
  .contact-list {
    position: absolute; left: 544px; top: 1036px; list-style: none;
    font-family: "Roboto Condensed", Arial, sans-serif; font-size: 13px;
    color: var(--white); letter-spacing: .4px;
  }
  .contact-list li { display: flex; align-items: center; gap: 8px; height: 28px; }
  .contact-list svg { width: 17px; height: 17px; }
</style>
</head>
<body>
<main class="poster">
  <div class="band-top"></div>
  <div class="photo" role="img" aria-label="Photo of a mother hugging her young child beside packed cardboard boxes near a yellow front door"></div>
  <svg class="torn torn-coral" viewBox="0 0 740 70" preserveAspectRatio="none" aria-hidden="true">
    <path d="M0 0H740V42L700 40 660 46 610 38 570 44 520 36 470 44 420 38 380 30 340 40 290 34 240 42 190 36 140 44 90 38 40 44 0 38Z" fill="#cd5f4c"/>
    <path d="M0 38L40 44 90 38 140 44 190 36 240 42 290 34 340 40 380 30 420 38 470 44 520 36 570 44 610 38 660 46 700 40 740 42V48L700 46 660 52 610 44 570 50 520 42 470 50 420 44 380 36 340 46 290 40 240 48 190 42 140 50 90 44 40 50 0 44Z" fill="#f1ece8"/>
  </svg>
  <svg class="torn torn-paper" viewBox="0 0 740 60" preserveAspectRatio="none" aria-hidden="true">
    <path d="M0 28L50 20 100 30 160 18 220 32 280 22 340 34 400 24 460 36 520 26 580 38 640 28 700 36 740 30V60H0Z" fill="#ededeb"/>
    <path d="M0 28L50 20 100 30 160 18 220 32 280 22 340 34 400 24 460 36 520 26 580 38 640 28 700 36 740 30V36L700 42 640 34 580 44 520 32 460 42 400 30 340 40 280 28 220 38 160 24 100 36 50 26 0 34Z" fill="#dcdcda"/>
  </svg>
  <div class="paper-strip"></div>
  <svg class="torn torn-navy" viewBox="0 0 740 60" preserveAspectRatio="none" aria-hidden="true">
    <path d="M0 6L40 12 90 8 140 16 200 10 260 20 320 14 380 22 440 12 500 18 560 8 620 14 680 6 740 10V60H0Z" fill="#2f4487"/>
    <path d="M0 22L60 28 110 34 140 40 90 36 30 30 0 30Z" fill="#ededeb"/>
    <path d="M660 20L700 16 740 14V20L700 24Z" fill="#ededeb"/>
  </svg>

  <div class="title-frame"><h1 class="title">EVICTION</h1></div>

  <p class="quote"><span class="mark open">&ldquo;</span>Everyone needs safe and suitable housing, whether they own a home or rent one.<br>When homelessness threatens, we at CCN help clients <strong>free of charge</strong> through eviction<br>diversion programs and mortgage/tax foreclosure prevention.<span class="mark close">&rdquo;</span></p>

  <div class="brand">
    <div class="brand-dot" aria-hidden="true"></div>
    <p class="brand-name">Civic Counsel and Advocacy<br>Network Incorporated</p>
  </div>

  <p class="tagline">We are<br><strong>YOUR Law Firm</strong><br>for Housing<br>Matters</p>

  <p class="contact-line">CONTACT US AT
    <span><svg viewBox="0 0 24 24" aria-hidden="true"><circle cx="12" cy="12" r="10.5" fill="none" stroke="#c9a24a" stroke-width="1.6"/><path d="M8.6 6.8l1.6-.3 1.2 2.8-1.1 1c.6 1.4 1.6 2.4 3 3.1l1-1.1 2.8 1.2-.3 1.6c-.2.6-.8 1-1.5.9-3.7-.6-6.9-3.8-7.5-7.5 0-.8.3-1.4.8-1.7z" fill="none" stroke="#c9a24a" stroke-width="1.4" stroke-linejoin="round"/></svg>(555) 314-2869</span>
  </p>

  <ul class="contact-list">
    <li><svg viewBox="0 0 20 20" aria-hidden="true"><rect x="2" y="4.5" width="16" height="11" fill="none" stroke="#fff" stroke-width="1.2"/><path d="M2 4.5l8 6.5 8-6.5M2 15.5l6-5.5M18 15.5l-6-5.5" fill="none" stroke="#fff" stroke-width="1.2"/></svg>housing@ccanmorvale.org</li>
    <li><svg viewBox="0 0 20 20" aria-hidden="true"><g fill="none" stroke="#fff" stroke-width="1.1"><circle cx="10" cy="10" r="8"/><ellipse cx="10" cy="10" rx="3.5" ry="8"/><path d="M2 10h16M3.5 6h13M3.5 14h13"/></g></svg>www.ccanmorvale.org</li>
  </ul>
</main>
</body>
</html>
```